New design for our website – modern, elegant, and customer-focused

We want to redesign our website, www.kalmenstrand.se, to create a completely new look that reflects the high quality of our products and services. We are seeking assistance in developing a modern, clean, and user-friendly web experience in Flatsome that strengthens our brand and makes it easier for customers to find the right solutions. Our goal is to enhance the design, functionality, and overall impression to better meet today’s expectations and demands.

Target Market(s)

swimmingpool & spa

Industry/Entity Type

Poolbusiness

Coding

Coded - Design and coding required

Number of Pages Required

1 page

Font styles to use
Other font styles liked:
• HaboroSoft

Requirements
Must have
• We working in Flatsome
Nice to have
• From dream to reality – swimming pools that transform your garden into a place of life and enjoyment.
Should not have
• Nice look

```html
<!DOCTYPE html>
<html lang="en">
<head>
<meta charset="utf-8">
<title>Kalmen Strand – From Dream to Reality</title>
<link href="https://fonts.googleapis.com/css2?family=Inter:wght@400;500;600;700;800&display=swap" rel="stylesheet">
<style>
:root{
  --navy:#0d3b5e;
  --deep:#0a2f4d;
  --blue:#0d8fdb;
  --sky:#1aa3e8;
  --light-blue:#7fd0f5;
  --ink:#111827;
  --muted:#5b6472;
  --sand:#f3f1ed;
  --white:#ffffff;
  --star:#f5b800;
}
*{box-sizing:border-box;margin:0;padding:0}
html,body{width:1200px;height:4748px;overflow:hidden}
body{font-family:"Inter",sans-serif;color:var(--ink);background:var(--white)}
a{color:inherit;text-decoration:none}
svg{display:block}

/* top bar */
.topbar{height:34px;background:var(--navy);color:#fff;font-size:12px;display:flex;align-items:center;justify-content:space-between;padding:0 30px}
.topbar .info{display:flex;gap:22px}
.topbar .info span{display:flex;align-items:center;gap:6px}
.dots{display:flex;gap:10px}
.dots i{width:10px;height:10px;border-radius:50%;background:#fff;display:block}

/* nav */
.nav{height:74px;display:flex;align-items:center;padding:0 30px;background:#fff;box-shadow:0 1px 4px rgba(0,0,0,.06);position:relative;z-index:2}
.brand{font-size:22px;font-weight:700;color:var(--blue);width:206px}
.menu{display:flex;gap:44px;font-size:14px;font-weight:500;color:var(--ink)}
.menu span{display:flex;align-items:center;gap:6px}
.btn-quote{margin-left:auto;background:var(--sky);color:#fff;font-weight:600;font-size:14px;padding:11px 20px;border-radius:22px;display:flex;gap:8px;align-items:center}

/* hero */
.hero{height:751px;position:relative;overflow:hidden}
.hero-photo{position:absolute;inset:0;background:
  linear-gradient(90deg,rgba(10,40,70,.75) 0%,rgba(10,40,70,.35) 55%,rgba(10,40,70,.1) 100%),
  linear-gradient(180deg,#3f6a4e 0%,#6f8c6a 35%,#8d8a7a 55%,#1aa0d8 72%,#147fb3 85%,#2d4a33 100%)}
.hero-content{position:absolute;left:30px;top:144px;color:#fff;width:620px}
.badge{display:inline-flex;align-items:center;gap:8px;background:rgba(255,255,255,.18);border-radius:20px;padding:8px 16px;font-size:12px;font-weight:600}
.hero h1{font-size:68px;line-height:1;font-weight:800;margin-top:26px;letter-spacing:-1px}
.hero h1 .accent{color:var(--light-blue);display:block}
.hero .lead{font-size:22px;line-height:1.3;margin-top:26px;width:620px}
.hero-actions{display:flex;gap:16px;margin-top:28px}
.btn{display:inline-flex;align-items:center;gap:8px;border-radius:30px;font-weight:600;font-size:16px;padding:18px 30px}
.btn-solid{background:var(--sky);color:#fff}
.btn-ghost{border:2px solid #fff;color:#fff}
.stats{display:flex;margin-top:46px}
.stat{width:218px;text-align:center}
.stat b{display:block;font-size:27px;font-weight:700}
.stat small{font-size:12px}
.hero .chev{position:absolute;left:600px;top:688px}

/* features */
.features{height:387px;background:var(--sand);display:flex;padding:89px 30px 0}
.feature{width:285px;text-align:center;padding:0 18px;margin-right:7px}
.icon-box{width:76px;height:76px;border-radius:10px;background:var(--sky);margin:0 auto 27px;display:flex;align-items:center;justify-content:center}
.feature h3{font-size:18px;font-weight:700;margin-bottom:14px;line-height:1.35}
.feature p{font-size:14px;color:var(--muted);line-height:1.6}

/* categories */
.categories{height:693px;text-align:center;padding-top:88px}
.section-title{font-size:44px;font-weight:700;letter-spacing:-.5px}
.section-title .accent{color:var(--blue)}
.section-sub{font-size:18px;color:var(--muted);margin-top:18px;line-height:1.5}
.cards{display:flex;gap:30px;padding:0 30px;margin-top:54px}
.cat-card{width:360px;height:360px;border-radius:12px;position:relative;overflow:hidden;text-align:left;color:#fff;box-shadow:0 8px 20px rgba(0,0,0,.15)}
.cat-card .photo{position:absolute;inset:0}
.cat-card .shade{position:absolute;inset:0;background:linear-gradient(180deg,rgba(13,59,94,0) 25%,rgba(13,59,94,.92) 100%)}
.cat-card .body{position:absolute;left:30px;right:30px;bottom:30px}
.cat-card h3{font-size:22px;font-weight:700}
.cat-card p{font-size:14px;line-height:1.6;margin-top:8px}
.cat-card .more{font-size:14px;font-weight:600;margin-top:12px;display:flex;gap:6px;align-items:center}

/* how it works */
.how{height:535px;background:linear-gradient(160deg,#0b4f82 0%,#0f74b4 55%,#13a0e6 100%);color:#fff;text-align:center;padding-top:86px}
.how .section-title{color:#fff}
.how .section-sub{color:#e6f4ff;margin-top:22px}
.steps{display:flex;padding:0 30px;margin-top:56px}
.step{width:285px;margin-right:7px;padding:0 22px}
.num{width:76px;height:76px;border-radius:50%;border:2px solid rgba(255,255,255,.6);background:rgba(255,255,255,.15);margin:0 auto 28px;display:flex;align-items:center;justify-content:center;font-size:28px;font-weight:600}
.step h3{font-size:18px;font-weight:700;margin-bottom:14px}
.step p{font-size:14px;line-height:1.6;color:#e1f1fc}

/* wellness */
.wellness{height:765px;position:relative}
.well-text{position:absolute;left:30px;top:91px;width:520px}
.tag{display:inline-block;background:#cfe9fb;color:var(--navy);font-size:12px;font-weight:600;padding:8px 22px;border-radius:18px}
.well-text h2{font-size:44px;line-height:1.05;font-weight:700;margin-top:24px;letter-spacing:-.5px}
.well-text .lead{font-size:18px;color:var(--muted);line-height:1.45;margin-top:24px}
.well-list{margin-top:22px}
.well-item{display:flex;gap:20px;margin-bottom:22px}
.well-item .ic{width:44px;height:44px;border-radius:8px;background:#d7eefc;flex:none;display:flex;align-items:center;justify-content:center}
.well-item h4{font-size:15px;font-weight:600}
.well-item p{font-size:14px;color:var(--muted);line-height:1.6;margin-top:10px}
.btn-small{display:inline-flex;align-items:center;gap:8px;background:var(--sky);color:#fff;font-weight:600;font-size:14px;padding:16px 30px;border-radius:26px;margin-top:10px;box-shadow:0 4px 10px rgba(26,163,232,.3)}
.tile{position:absolute;border-radius:10px;box-shadow:0 6px 16px rgba(0,0,0,.15)}
.t1{left:623px;top:91px;width:265px;height:242px;background:linear-gradient(135deg,#e9e6e1,#c9c2b6 60%,#d98aa9)}
.t2{left:623px;top:346px;width:265px;height:300px;background:linear-gradient(160deg,#f2e9df,#c99a78 55%,#8c8ba8)}
.t3{left:903px;top:121px;width:265px;height:299px;background:linear-gradient(180deg,#8d8d8d,#3a3a3a 60%,#1c1c1c)}
.t4{left:903px;top:436px;width:265px;height:238px;background:linear-gradient(160deg,#d6c6b4,#8a5a3a 50%,#3b2418)}

/* testimonials */
.testimonials{height:608px;background:var(--sand);text-align:center;padding-top:84px}
.quotes{display:flex;gap:30px;padding:0 30px;margin-top:60px}
.quote{width:360px;height:245px;background:#fff;border-radius:10px;box-shadow:0 4px 14px rgba(0,0,0,.08);text-align:left;padding:30px 30px}
.stars{display:flex;gap:3px}
.quote blockquote{font-style:italic;font-size:14px;line-height:1.6;color:var(--muted);margin-top:16px}
.person{display:flex;align-items:center;gap:16px;margin-top:20px}
.avatar{width:44px;height:44px;border-radius:50%;background:#d7eefc;color:var(--navy);font-weight:700;font-size:14px;display:flex;align-items:center;justify-content:center}
.person b{font-size:14px;display:block}
.person small{font-size:12px;color:#8a8f97}

/* cta */
.cta{height:442px;background:linear-gradient(180deg,#12a5e4,#0d8ed4);color:#fff;text-align:center;padding-top:80px}
.cta h2{font-size:44px;line-height:1.05;font-weight:700;width:880px;margin:0 auto}
.cta p{font-size:18px;line-height:1.5;width:720px;margin:22px auto 0}
.cta-actions{display:flex;gap:16px;justify-content:center;margin-top:38px}
.btn-white{background:#fff;color:var(--blue)}

/* footer */
.footer{height:459px;background:var(--deep);color:#d4e1ec;padding:64px 30px 0;position:relative}
.foot-cols{display:flex}
.foot-col{width:293px}
.foot-col h4{color:#fff;font-size:15px;font-weight:600;margin-bottom:26px}
.foot-brand{font-size:22px;font-weight:700;color:#fff;margin-bottom:26px}
.foot-col p{font-size:14px;line-height:1.6;width:260px}
.foot-col ul{list-style:none}
.foot-col li{font-size:14px;margin-bottom:18px}
.contact li{display:flex;gap:12px}
.socials{display:flex;gap:16px;margin-top:26px}
.socials i{width:36px;height:36px;border-radius:50%;background:#1c4a70;display:block}
.copyright{position:absolute;left:30px;right:30px;bottom:64px;border-top:1px solid #1f4c72;padding-top:30px;text-align:center;font-size:13px}
</style>
</head>
<body>

<div class="topbar">
  <div class="info">
    <span><svg width="12" height="12" viewBox="0 0 24 24" fill="#fff"><path d="M6.6 10.8a15 15 0 006.6 6.6l2.2-2.2a1 1 0 011-.25 11 11 0 003.5.56 1 1 0 011 1V20a1 1 0 01-1 1A17 17 0 013 4a1 1 0 011-1h3.5a1 1 0 011 1c0 1.2.2 2.4.56 3.5a1 1 0 01-.25 1z"/></svg>+46 (0)8 555 010 20</span>
    <span><svg width="12" height="12" viewBox="0 0 24 24" fill="#fff"><path d="M2 5h20v14H2z" opacity=".9"/><path d="M2 5l10 8 10-8" stroke="#0d3b5e" stroke-width="2" fill="none"/></svg>info@kalmenstrand.se</span>
  </div>
  <div class="dots"><i></i><i></i><i></i></div>
</div>

<nav class="nav">
  <div class="brand">Kalmen Strand</div>
  <div class="menu">
    <span>Home</span>
    <span>Pools <svg width="10" height="10" viewBox="0 0 10 10"><path d="M2 3.5l3 3 3-3" stroke="#111" stroke-width="1.4" fill="none"/></svg></span>
    <span>Spa &amp; Wellness <svg width="10" height="10" viewBox="0 0 10 10"><path d="M2 3.5l3 3 3-3" stroke="#111" stroke-width="1.4" fill="none"/></svg></span>
    <span>Services <svg width="10" height="10" viewBox="0 0 10 10"><path d="M2 3.5l3 3 3-3" stroke="#111" stroke-width="1.4" fill="none"/></svg></span>
    <span>Project</span>
    <span>About Us</span>
    <span>Contact</span>
  </div>
  <a class="btn-quote"><svg width="12" height="14" viewBox="0 0 12 14"><rect x="1" y="1" width="10" height="12" rx="1.5" stroke="#fff" stroke-width="1.6" fill="none"/><path d="M3.5 5h5M3.5 8h5" stroke="#fff" stroke-width="1.4"/></svg>Get Quote</a>
</nav>

<header class="hero">
  <div class="hero-photo" role="img" aria-label="Garden swimming pool with stone walls, trees and a sun umbrella"></div>
  <div class="hero-content">
    <span class="badge"><svg width="12" height="12" viewBox="0 0 24 24" fill="#f5b800"><path d="M12 2l3 7 7 .6-5.4 4.7 1.7 7.2L12 17.8 5.7 21.5l1.7-7.2L2 9.6 9 9z"/></svg>Sweden's Leading Pool Supplier</span>
    <h1>From Dream to<span class="accent">Reality</span></h1>
    <p class="lead">Swimming pools that transform your garden into a place for life and enjoyment</p>
    <div class="hero-actions">
      <a class="btn btn-solid"><svg width="12" height="14" viewBox="0 0 12 14"><rect x="1" y="1" width="10" height="12" rx="1.5" stroke="#fff" stroke-width="1.6" fill="none"/><path d="M3.5 5h5M3.5 8h5" stroke="#fff" stroke-width="1.4"/></svg>Get Free Quote</a>
      <a class="btn btn-ghost"><svg width="16" height="14" viewBox="0 0 16 14"><rect x="1" y="3" width="12" height="9" rx="1.5" stroke="#fff" stroke-width="1.6" fill="none"/><path d="M4 1h11v8" stroke="#fff" stroke-width="1.4" fill="none"/></svg>See Our Projects</a>
    </div>
    <div class="stats">
      <div class="stat"><b>500+</b><small>Installed Pools</small></div>
      <div class="stat"><b>15+</b><small>Years of Experience</small></div>
      <div class="stat"><b>100%</b><small>Satisfied Customers</small></div>
    </div>
  </div>
  <svg class="chev" width="22" height="14" viewBox="0 0 22 14"><path d="M3 3l8 8 8-8" stroke="#fff" stroke-width="2.4" fill="none"/></svg>
</header>

<section class="features">
  <div class="feature">
    <div class="icon-box"><svg width="30" height="30" viewBox="0 0 24 24" fill="none" stroke="#fff" stroke-width="2"><circle cx="12" cy="9" r="6"/><path d="M8.5 14l-1.5 8 5-3 5 3-1.5-8"/></svg></div>
    <h3>Premium quality</h3>
    <p>Only high-quality materials and components from leading manufacturers</p>
  </div>
  <div class="feature">
    <div class="icon-box"><svg width="30" height="30" viewBox="0 0 24 24" fill="none" stroke="#fff" stroke-width="2.2"><path d="M4 4l16 16M20 4L4 20"/><circle cx="6" cy="6" r="2.5"/><circle cx="18" cy="18" r="2.5"/></svg></div>
    <h3>Professional Installation</h3>
    <p>Experienced installers who guarantee perfect results</p>
  </div>
  <div class="feature">
    <div class="icon-box"><svg width="30" height="30" viewBox="0 0 24 24" fill="none" stroke="#fff" stroke-width="2.2"><path d="M4 14v-2a8 8 0 0116 0v2"/><rect x="3" y="13" width="4" height="6" rx="1.5"/><rect x="17" y="13" width="4" height="6" rx="1.5"/></svg></div>
    <h3>Lifetime warranty</h3>
    <p>Comprehensive warranty and support for the entire life of the pool</p>
  </div>
  <div class="feature">
    <div class="icon-box"><svg width="30" height="30" viewBox="0 0 24 24" fill="#fff"><path d="M20 4C9 4 4 9 4 16c0 1 .2 2 .5 3 3-6 7-9 11-10-4 2-7 5-9 10 1 .5 2 .8 3.5.8C17 19.8 20 13 20 4z"/></svg></div>
    <h3>Environmentally Friendly Solutions</h3>
    <p>Energy-efficient systems that are kind to the environment</p>
  </div>
</section>

<section class="categories">
  <h2 class="section-title">Our <span class="accent">Pool Categories</span></h2>
  <p class="section-sub">We offer a wide range of pools for all needs and preferences.</p>
  <div class="cards">
    <article class="cat-card">
      <div class="photo" role="img" aria-label="City skyline at dusk seen from an indoor pool" style="background:linear-gradient(180deg,#7f93a8,#4b5d78 45%,#2b3c5c)"></div>
      <div class="shade"></div>
      <div class="body"><h3>Indoor pools</h3><p>Enjoy swimming all year round in your own private oasis</p><span class="more">Read more <svg width="12" height="10" viewBox="0 0 12 10"><path d="M1 5h9M6 1l4 4-4 4" stroke="#fff" stroke-width="1.6" fill="none"/></svg></span></div>
    </article>
    <article class="cat-card">
      <div class="photo" role="img" aria-label="Outdoor pool with palm trees overlooking a city" style="background:linear-gradient(180deg,#c9d9e4,#8aa7b8 40%,#3f7ea0 70%,#1f5f86)"></div>
      <div class="shade"></div>
      <div class="body"><h3>Outdoor pools</h3><p>Perfect for sunny summer days in the garden</p><span class="more">Read more <svg width="12" height="10" viewBox="0 0 12 10"><path d="M1 5h9M6 1l4 4-4 4" stroke="#fff" stroke-width="1.6" fill="none"/></svg></span></div>
    </article>
    <article class="cat-card">
      <div class="photo" role="img" aria-label="Infinity pool merging with the sea horizon under an umbrella" style="background:linear-gradient(180deg,#b6c6cf,#87a2ad 40%,#4e8aa3 65%,#22607f)"></div>
      <div class="shade"></div>
      <div class="body"><h3>Infinity Pools</h3><p>Spectacular design that merges with the horizon</p><span class="more">Read more <svg width="12" height="10" viewBox="0 0 12 10"><path d="M1 5h9M6 1l4 4-4 4" stroke="#fff" stroke-width="1.6" fill="none"/></svg></span></div>
    </article>
  </div>
</section>

<section class="how">
  <h2 class="section-title">How It Works</h2>
  <p class="section-sub">From first contact to finished pool - we guide you through the entire process</p>
  <div class="steps">
    <div class="step"><div class="num">1</div><h3>Consultation</h3><p>We discuss your wishes and needs to find the perfect solution.</p></div>
    <div class="step"><div class="num">2</div><h3>Design &amp; Planning</h3><p>We create a customized design and detailed project plan</p></div>
    <div class="step"><div class="num">3</div><h3>Installation</h3><p>Professional installation by experienced specialists</p></div>
    <div class="step"><div class="num">4</div><h3>Support &amp; Service</h3><p>Continuous support and maintenance service after installation</p></div>
  </div>
</section>

<section class="wellness">
  <div class="well-text">
    <span class="tag">SPA &amp; WELLNESS</span>
    <h2>Complete Wellness for Your Home</h2>
    <p class="lead">Expand your pool with a hot tub, sauna and other wellness solutions for the ultimate relaxation experience.</p>
    <div class="well-list">
      <div class="well-item"><div class="ic"><svg width="20" height="20" viewBox="0 0 24 24" fill="none" stroke="#1aa3e8" stroke-width="2"><path d="M3 12h18v4a4 4 0 01-4 4H7a4 4 0 01-4-4z"/><path d="M6 12V5a2 2 0 014 0"/></svg></div><div><h4>Luxurious Spa Baths</h4><p>Premium spa with advanced hydrotherapy and energy-efficient technology</p></div></div>
      <div class="well-item"><div class="ic"><svg width="20" height="20" viewBox="0 0 24 24" fill="#1aa3e8"><path d="M12 3c3 4 6 7 6 11a6 6 0 01-12 0c0-4 3-7 6-11z"/></svg></div><div><h4>Traditional &amp; Infrared Saunas</h4><p>High-quality saunas in various sizes and designs</p></div></div>
      <div class="well-item"><div class="ic"><svg width="20" height="20" viewBox="0 0 24 24" fill="#1aa3e8"><path d="M12 4c2 3 2 7 0 10-2-3-2-7 0-10zM4 9c4 0 7 3 8 6-4 0-7-2-8-6zm16 0c-1 4-4 6-8 6 1-3 4-6 8-6zM5 18h14v2H5z"/></svg></div><div><h4>Wellness accessories</h4><p>Everything from lighting to sound systems for the perfect atmosphere</p></div></div>
    </div>
    <a class="btn-small">Explore Spa &amp; Wellness <svg width="12" height="10" viewBox="0 0 12 10"><path d="M1 5h9M6 1l4 4-4 4" stroke="#fff" stroke-width="1.6" fill="none"/></svg></a>
  </div>
  <div class="tile t1" role="img" aria-label="Spa towels, lotion bottle, candle and pink tulips"></div>
  <div class="tile t2" role="img" aria-label="Aromatic oil being poured during a massage"></div>
  <div class="tile t3" role="img" aria-label="Modern home gym with training equipment"></div>
  <div class="tile t4" role="img" aria-label="Hot stone massage with white flowers"></div>
</section>

<section class="testimonials">
  <h2 class="section-title">What Our Customers Say</h2>
  <p class="section-sub">Read about experiences from satisfied customers who have made their pool<br>dreams come true</p>
  <div class="quotes">
    <article class="quote">
      <div class="stars"><svg width="84" height="14" viewBox="0 0 84 14" fill="#f5b800"><g id="s"><path d="M7 0l2 4.6 5 .4-3.8 3.3 1.2 4.9L7 10.6 2.6 13.2l1.2-4.9L0 5l5-.4z"/></g><use href="#s" x="17"/><use href="#s" x="34"/><use href="#s" x="51"/><use href="#s" x="68"/></svg></div>
      <blockquote>"Kalmen Strand delivered a fantastic pool that exceeded all our expectations. Professional team and perfect result!"</blockquote>
      <div class="person"><div class="avatar">LB</div><div><b>Lena Berg</b><small>Stockholm</small></div></div>
    </article>
    <article class="quote">
      <div class="stars"><svg width="84" height="14" viewBox="0 0 84 14" fill="#f5b800"><use href="#s"/><use href="#s" x="17"/><use href="#s" x="34"/><use href="#s" x="51"/><use href="#s" x="68"/></svg></div>
      <blockquote>"From the first meeting to the finished pool, everything was smooth and professional. We love our new pool and can highly recommend Kalmen Strand!"</blockquote>
      <div class="person"><div class="avatar">JE</div><div><b>Johan Ekholm</b><small>Gothenburg</small></div></div>
    </article>
    <article class="quote">
      <div class="stars"><svg width="84" height="14" viewBox="0 0 84 14" fill="#f5b800"><use href="#s"/><use href="#s" x="17"/><use href="#s" x="34"/><use href="#s" x="51"/><use href="#s" x="68"/></svg></div>
      <blockquote>"Best investment we've made! The pool has become the family's favorite spot. Thanks for a fantastic job!"</blockquote>
      <div class="person"><div class="avatar">SH</div><div><b>Sara Holmqvist</b><small>Malmo</small></div></div>
    </article>
  </div>
</section>

<section class="cta">
  <h2>Ready to Make Your Pool Dream Come True?</h2>
  <p>Contact us today for a free consultation and quote. We will help you create the perfect pool for your home.</p>
  <div class="cta-actions">
    <a class="btn btn-white"><svg width="12" height="14" viewBox="0 0 12 14"><rect x="1" y="1" width="10" height="12" rx="1.5" stroke="#0d8fdb" stroke-width="1.6" fill="none"/><path d="M3.5 5h5M3.5 8h5" stroke="#0d8fdb" stroke-width="1.4"/></svg>Get Free Quote</a>
    <a class="btn btn-ghost"><svg width="14" height="14" viewBox="0 0 24 24" fill="#fff"><path d="M6.6 10.8a15 15 0 006.6 6.6l2.2-2.2a1 1 0 011-.25 11 11 0 003.5.56 1 1 0 011 1V20a1 1 0 01-1 1A17 17 0 013 4a1 1 0 011-1h3.5a1 1 0 011 1c0 1.2.2 2.4.56 3.5a1 1 0 01-.25 1z"/></svg>Call Us Now</a>
  </div>
</section>

<footer class="footer">
  <div class="foot-cols">
    <div class="foot-col">
      <div class="foot-brand">Kalmen Strand</div>
      <p>Sweden's leading supplier of high-quality pools and spa solutions since 2008.</p>
      <div class="socials"><i></i><i></i><i></i><i></i></div>
    </div>
    <div class="foot-col">
      <h4>Quick links</h4>
      <ul><li>About Us</li><li>Our Pools</li><li>Spa &amp; Wellness</li><li>Services</li><li>Project</li><li>Contact</li></ul>
    </div>
    <div class="foot-col">
      <h4>Our Services</h4>
      <ul><li>Pool installation</li><li>Maintenance &amp; Service</li><li>Repairs</li><li>Consultation</li><li>Accessories</li><li>Guarantees</li></ul>
    </div>
    <div class="foot-col contact">
      <h4>Contact Us</h4>
      <ul>
        <li><svg width="12" height="14" viewBox="0 0 24 24" fill="#fff"><path d="M12 2a7 7 0 017 7c0 5-7 13-7 13S5 14 5 9a7 7 0 017-7zm0 4a3 3 0 100 6 3 3 0 000-6z"/></svg><span>Badvägen 7<br>111 22 Stockholm</span></li>
        <li><svg width="12" height="14" viewBox="0 0 24 24" fill="#fff"><path d="M6.6 10.8a15 15 0 006.6 6.6l2.2-2.2a1 1 0 011-.25 11 11 0 003.5.56 1 1 0 011 1V20a1 1 0 01-1 1A17 17 0 013 4a1 1 0 011-1h3.5a1 1 0 011 1c0 1.2.2 2.4.56 3.5a1 1 0 01-.25 1z"/></svg>+46 (0)8 555 010 20</li>
        <li><svg width="12" height="14" viewBox="0 0 24 24" fill="#fff"><path d="M2 5h20v14H2z"/><path d="M2 5l10 8 10-8" stroke="#0a2f4d" stroke-width="2" fill="none"/></svg>info@kalmenstrand.se</li>
        <li><svg width="12" height="14" viewBox="0 0 24 24"><circle cx="12" cy="12" r="10" fill="#fff"/><path d="M12 6v6l4 2" stroke="#0a2f4d" stroke-width="2" fill="none"/></svg>Mon-Fri: 08:00-17:00</li>
      </ul>
    </div>
  </div>
  <div class="copyright">© 2024 Kalmen Strand AB. All rights reserved. | Corporate ID: 559870-0000</div>
</footer>

</body>
</html>
```